Chimney Service company needs new business card design

We need a updated business card with our new logo added. We provide a full range of chimney services throughout Vermont and New Hampshire. The business card will be one sided and color. Attached is our current business card another document showing all the information we would like on the card.
We dont like a lot of flashy colors.... here is a link to our website to get an idea of our branding www.flueguardianvt.example

Target Market(s)

homeowners

Industry/Entity Type

Business

Contact Information for Business Card

See attached sheet for content.

Font styles to use
Serif
Sans Serif

Requirements
Must have
• all information provided on separate sheet
Should not have
• Additional information that may clogg up design

```html
<!DOCTYPE html>
<html lang="en">
<head>
<meta charset="UTF-8">
<title>Flue Guardian – Business Card</title>
<link href="https://fonts.googleapis.com/css2?family=Cormorant+SC:wght@600&family=Open+Sans:ital,wght@0,400;1,400&display=swap" rel="stylesheet">
<style>
  :root {
    --backdrop: #e9e6e1;
    --card: #ffffff;
    --brick-red: #a5121b;
    --charcoal: #2f2f31;
    --ink: #262626;
    --on-dark: #ffffff;
  }
  * { box-sizing: border-box; margin: 0; padding: 0; }
  html, body {
    width: 1200px; height: 800px; overflow: hidden;
    background: var(--backdrop);
  }
  .business-card {
    position: absolute; left: 120px; top: 126px;
    width: 960px; height: 548px;
    background: var(--card);
    box-shadow: 0 6px 20px rgba(0,0,0,0.15);
    overflow: hidden;
    color: var(--ink);
  }
  .accent-bar {
    position: absolute; left: 0; top: 34px;
    width: 500px; height: 20px;
    background: var(--brick-red);
  }
  .accent-rule {
    position: absolute; left: 500px; right: 0; top: 52px;
    height: 2px; background: var(--brick-red);
  }
  .service-area {
    position: absolute; right: 0; top: 22px;
    display: flex; align-items: stretch;
    font-family: "Open Sans", sans-serif; font-style: italic;
    font-size: 19px; line-height: 32px;
  }
  .service-area .since-year {
    margin-left: 6px; padding: 0 10px;
    background: var(--brick-red); color: var(--on-dark);
    font-style: normal;
  }
  .brand {
    position: absolute; left: 60px; top: 110px; width: 370px;
    text-align: center;
  }
  .brand-square {
    display: block; margin: 0 auto 26px;
    width: 110px; height: 110px;
    background: var(--charcoal);
  }
  .brand-name {
    font-family: "Cormorant SC", serif; font-weight: 600;
    font-size: 40px; line-height: 44px; letter-spacing: 1px;
    color: var(--ink); white-space: nowrap;
  }
  .assurances {
    position: absolute; left: 520px; top: 150px;
    font-family: "Cormorant SC", serif; font-weight: 600;
    font-size: 27px; line-height: 30px; letter-spacing: 0.5px;
  }
  .contact {
    position: absolute; left: 520px; top: 250px;
    list-style: none;
    font-family: "Cormorant SC", serif; font-weight: 600;
    font-size: 23px; line-height: 29px; letter-spacing: 0.5px;
  }
  .services-band {
    position: absolute; left: 0; right: 0; top: 378px; height: 130px;
    background: var(--charcoal);
    display: flex; justify-content: space-around; align-items: center;
    padding: 0 20px;
    list-style: none;
  }
  .services-band li {
    color: var(--on-dark); text-align: center;
    font-family: "Open Sans", sans-serif; font-size: 20px; line-height: 27px;
  }
  .footer-band {
    position: absolute; left: 0; right: 0; top: 508px; bottom: 0;
    background: var(--brick-red);
  }
</style>
</head>
<body>
  <article class="business-card">
    <div class="accent-bar"></div>
    <div class="accent-rule"></div>
    <p class="service-area">Serving VT and New Hampshire since <span class="since-year">1989</span></p>

    <header class="brand">
      <span class="brand-square"></span>
      <h1 class="brand-name">Flue Guardian</h1>
    </header>

    <p class="assurances">Fully Insured – Free Estimate<br>Family owned and operated</p>

    <ul class="contact">
      <li>802-555-0147</li>
      <li>info@flueguardianvt.example</li>
      <li>www.flueguardianvt.example</li>
    </ul>

    <ul class="services-band">
      <li>Full Masonry<br>Services</li>
      <li>Historic chimney<br>restoration</li>
      <li>Stainless steel<br>liners</li>
      <li>New Chimney<br>installations</li>
      <li>Guild Certified<br>Chimney sweeps</li>
    </ul>
    <div class="footer-band"></div>
  </article>
</body>
</html>
```